Powerpoint and Word Document Template

Our target market are C-suite executives in banks, credit unions, non-bank financial institutions, financial technology companies and in the law firms, private equity firms and the like that are also advising the industry.

design should convey: confidence, trust, expertise, experience, value, advice, relationship focus.

For the stationery design, we will need the .doc format as well.

Industry/Entity Type

Consulting

Font styles to use
Sans Serif

Colors
0356a4
3277b5
85acd3
cedeed
eaf1f7
ffffff

Requirements
Must have
• must use the logo and color scheme included in the attached zip file. must include a powerpoint template with a cover slide, section break slides, slides for images/graphics, slides for side by side content, and slides for regular content.

Note: this should also include designs for word documents like stationary and envelopes based on the same concept.

```html
<!DOCTYPE html>
<html lang="en">
<head>
<meta charset="utf-8">
<title>Corvane Advisory – Cover Slide</title>
<link href="https://fonts.googleapis.com/css2?family=Open+Sans:wght@400;700&display=swap" rel="stylesheet">
<style>
  :root {
    --brand-blue: #0356a4;
    --brand-blue-deep: #0a4a8c;
    --brand-blue-mid: #3277b5;
    --accent-gold: #fbb12b;
    --white: #ffffff;
    --photo-light: #efe2cf;
    --photo-dark: #2a3440;
  }
  html, body {
    margin: 0;
    padding: 0;
    width: 1200px;
    height: 675px;
    overflow: hidden;
    background: var(--white);
  }
  .cover-slide {
    position: relative;
    width: 1200px;
    height: 675px;
    overflow: hidden;
    background: linear-gradient(180deg, #1b5c97 0%, var(--brand-blue) 55%, var(--brand-blue-deep) 100%);
    font-family: "Open Sans", Arial, sans-serif;
  }
  .slide-shapes {
    position: absolute;
    inset: 0;
    width: 1200px;
    height: 675px;
  }
  .brand-lockup {
    position: absolute;
    left: 72px;
    top: 170px;
    display: flex;
    align-items: center;
    gap: 30px;
    color: var(--white);
  }
  .brand-mark {
    width: 106px;
    height: 106px;
    border: 5px solid var(--white);
    box-sizing: border-box;
  }
  .brand-name {
    display: flex;
    flex-direction: column;
    font-weight: 400;
    color: var(--white);
    line-height: 1;
  }
  .brand-name__primary {
    font-size: 66px;
    letter-spacing: 1px;
  }
  .brand-name__secondary {
    font-size: 22px;
    letter-spacing: 11px;
    margin-top: 8px;
    padding-left: 74px;
  }
  .cover-title {
    position: absolute;
    left: 99px;
    top: 340px;
    margin: 0;
    font-weight: 700;
    font-size: 43px;
    line-height: 55px;
    color: var(--white);
    text-transform: uppercase;
    letter-spacing: -0.5px;
  }
</style>
</head>
<body>
  <main class="cover-slide">
    <svg class="slide-shapes" viewBox="0 0 1200 675" xmlns="http://www.w3.org/2000/svg">
      <defs>
        <linearGradient id="photoTone" x1="0" y1="0" x2="0.4" y2="1">
          <stop offset="0" stop-color="#efe2cf"/>
          <stop offset="0.45" stop-color="#8a7a68"/>
          <stop offset="1" stop-color="#2a3440"/>
        </linearGradient>
      </defs>
      <polygon class="hero-photo" role="img"
        aria-label="Photo of two advisors in suits reviewing documents and a tablet at a meeting table"
        points="862,0 1200,0 1200,675 456,675" fill="url(#photoTone)"/>
      <polygon class="title-band" points="70,311 684,311 572,483 70,483" fill="var(--accent-gold)"/>
      <polygon class="accent-stripe accent-stripe--long" points="806,131 824,131 531,591 505,591" fill="var(--accent-gold)"/>
      <polygon class="accent-stripe accent-stripe--upper" points="900,33 925,33 633,493 605,493" fill="var(--accent-gold)"/>
      <polygon class="accent-corner" points="1200,416 1200,675 1038,675" fill="var(--accent-gold)"/>
    </svg>

    <div class="brand-lockup">
      <div class="brand-mark"></div>
      <div class="brand-name">
        <span class="brand-name__primary">CORVANE</span>
        <span class="brand-name__secondary">ADVISORY</span>
      </div>
    </div>

    <h1 class="cover-title">Persentatoin<br>Template Title Here</h1>
  </main>
</body>
</html>
```